GLOW ON THE AVENUE WEBSITE

I have a website www.glowontheavenue.org , need information from that jazzed up. wanted page to be fun & funky .

Target Market(s)

18 to 35yrs guys & girls

Requirements
Must have
• use all photos on website, need to attached my brochure for printing

```html
<!DOCTYPE html>
<html lang="en">
<head>
<meta charset="utf-8">
<title>Glow on the Avenue</title>
<link href="https://fonts.googleapis.com/css2?family=Comfortaa:wght@300;400;700&display=swap" rel="stylesheet">
<style>
  :root {
    --red: #c80000;
    --deep-red: #b00000;
    --black: #000000;
    --white: #ffffff;
    --yellow: #f2e01a;
    --pink: #f4a0b0;
    --text-dark: #1a1a1a;
    --thin: "Comfortaa", sans-serif;
    --plain: Arial, Helvetica, sans-serif;
  }
  * { box-sizing: border-box; margin: 0; padding: 0; }
  html, body { width: 858px; height: 1200px; overflow: hidden; background: var(--red); }
  .page { position: relative; width: 858px; height: 1200px; background: var(--red); font-family: var(--thin); }

  .header-photo {
    position: absolute; left: 0; top: 0; width: 858px; height: 278px;
    background: linear-gradient(100deg, #2a2a2a 0%, #1a1a1a 35%, #8a0a0a 60%, #d01010 80%, #3a0a0a 100%);
  }
  .header-rule { position: absolute; left: 0; top: 278px; width: 858px; height: 14px; background: #1c0505; }

  .brand-tab {
    position: absolute; left: 68px; top: 233px; width: 149px; height: 70px;
    background: var(--white); border-radius: 6px 6px 0 0;
    display: flex; align-items: center; justify-content: center; text-align: center;
  }
  .brand-name { font-family: var(--thin); font-weight: 700; font-size: 15px; line-height: 1.15; color: var(--red); }

  .side-panel {
    position: absolute; left: 8px; top: 301px; width: 258px; height: 501px;
    background: var(--white); border-radius: 8px;
  }
  .side-nav { position: absolute; left: 33px; top: 27px; list-style: none; }
  .side-nav li { font-family: var(--thin); font-weight: 300; font-size: 19px; line-height: 25.3px; color: var(--text-dark); }

  .inquire { position: absolute; left: 30px; top: 305px; font-family: var(--plain); font-size: 25px; color: var(--red); letter-spacing: -0.3px; }
  .address { position: absolute; left: 32px; font-family: var(--plain); font-size: 11.5px; line-height: 15px; color: var(--black); }
  .address.one { top: 353px; }
  .address.two { top: 411px; }

  .hero-title { position: absolute; left: 299px; top: 395px; color: var(--white); }
  .hero-title .lead { font-weight: 300; font-size: 35px; line-height: 40px; }
  .hero-title .strong { font-weight: 700; font-size: 26px; line-height: 32px; margin-left: 2px; }
  .hero-offer { position: absolute; left: 303px; top: 482px; font-size: 18px; color: var(--yellow); font-weight: 400; }

  .photo-woman {
    position: absolute; left: 630px; top: 311px; width: 224px; height: 302px;
    background: radial-gradient(ellipse at 45% 50%, #e9c2a6 0%, #d89c80 40%, rgba(200,0,0,0) 72%);
  }

  .promo { position: absolute; left: 293px; top: 615px; width: 515px; height: 114px; border-radius: 8px; overflow: hidden; display: flex; }
  .promo-offer {
    width: 267px; background: var(--black); color: var(--yellow);
    font-size: 35px; line-height: 41px; text-align: center; padding-top: 18px; font-weight: 400;
  }
  .promo-call {
    flex: 1; background: var(--white); color: var(--red);
    font-size: 26px; line-height: 29px; padding: 12px 0 0 30px; font-weight: 400;
  }

  .photo-man {
    position: absolute; left: 280px; top: 762px; width: 293px; height: 275px;
    background: radial-gradient(ellipse at 50% 50%, #e0a888 0%, #c98a6c 42%, rgba(200,0,0,0) 72%);
  }

  .mens-title { position: absolute; left: 595px; top: 786px; font-weight: 300; font-size: 27px; color: var(--white); }
  .mens-list { position: absolute; left: 614px; top: 843px; list-style: none; }
  .mens-list li { font-weight: 700; font-size: 21px; line-height: 25.3px; color: var(--white); }
  .more-button {
    position: absolute; left: 611px; top: 981px; width: 112px; height: 30px;
    background: var(--black); color: var(--white); border-radius: 8px;
    font-size: 12px; display: flex; align-items: center; justify-content: center;
  }

  .footer { position: absolute; left: 0; top: 1042px; width: 858px; height: 118px; background: var(--black); text-align: center; }
  .footer-links { margin-top: 23px; font-family: var(--plain); font-size: 10.5px; color: var(--white); }
  .copyright { margin-top: 8px; font-family: var(--plain); font-size: 9px; color: var(--pink); }
  .footer-brand { margin-top: 15px; font-family: var(--thin); font-weight: 700; font-size: 15px; color: var(--pink); }
</style>
</head>
<body>
<div class="page">
  <div class="header-photo" role="img" aria-label="Banner photograph of a smiling woman and a pair of legs in stockings and heels on red fabric"></div>
  <div class="header-rule"></div>

  <div class="brand-tab"><span class="brand-name">Glow on<br>the Avenue</span></div>

  <aside class="side-panel">
    <ul class="side-nav">
      <li>Waxing</li>
      <li>City brow bar</li>
      <li>Eyes incl. Lash extensions</li>
      <li>Tanning</li>
      <li>Hands &amp; Feet</li>
      <li>Facial &amp; Massage</li>
      <li>Makeup</li>
      <li>Specials</li>
      <li>Products</li>
      <li>Blog</li>
    </ul>
    <h2 class="inquire">INQUIRE NOW!</h2>
    <p class="address one">Australia NSW -120<br>Harbour Rd Kelmore<br>2281- 02 4900 1234</p>
    <p class="address two">Australia NSW -47<br>Harbour Rd Ashvale<br>2291 -02 4900 5678</p>
  </aside>

  <h1 class="hero-title"><div class="lead">We are the Best in</div><div class="strong">Wax Down Under</div></h1>
  <p class="hero-offer">Brazilians from $39.00</p>
  <div class="photo-woman" role="img" aria-label="Photograph of a seated woman with a flower in her hair beside a straw hat"></div>

  <div class="promo">
    <div class="promo-offer">20% OFF<br>ALL WAXING</div>
    <div class="promo-call">WAX ME<br>WEDNESDAYS<br>Call TODAY!</div>
  </div>

  <div class="photo-man" role="img" aria-label="Photograph of a shirtless man in sunglasses flexing his arms"></div>
  <h2 class="mens-title">Specializes in men’s</h2>
  <ul class="mens-list">
    <li>Underarms</li>
    <li>Full Arms</li>
    <li>Top Arms</li>
    <li>Chest</li>
    <li>Stomach</li>
  </ul>
  <div class="more-button">other services</div>

  <footer class="footer">
    <p class="footer-links">Home | Waxing | City brow bar | Eyes incl. Lash extensions | Tanning | Hands &amp; Feet | Facials &amp; Massage | Makeup | Specials | Products | Blog | Contact Us</p>
    <p class="copyright">Copyright © 2013 Glow on the Avenue. All Rights Reserved</p>
    <p class="footer-brand">Glow on the Avenue</p>
  </footer>
</div>
</body>
</html>
```